Storm Restoration Contractor needs a professional letterhead design

Looking for a professional letterhead design. Not looking for your cheapo MS Word standard ones that are readily available. Dont want it to be cookie cutter look like ones readily available online. We just recently changed our logo and want to freshen up all our documents. Our company handles restoring a property back to a pre-loss condition after a storm damages it. For example, wind, hail, flood, fire losses.

Target Market(s)

Property Owners, Homeowners, Property Owners, Commercial Property Owners, Property Management Companies

Industry/Entity Type

Construction Company

Requirements
Must have
• Professional, Use 1 of 2 logo options
• Storm Restoration, Roofing, Siding, Windows

```html
<!DOCTYPE html>
<html lang="en">
<head>
<meta charset="utf-8">
<title>Restora Homeworks Letterhead</title>
<link href="https://fonts.googleapis.com/css2?family=Open+Sans:wght@300;400;600&display=swap" rel="stylesheet">
<style>
  :root {
    --backdrop: #e8e9eb;
    --paper: #ffffff;
    --navy: #0a1f6b;
    --deep-blue: #0b3fa0;
    --brand-blue: #1b82cc;
    --sky-blue: #2f9ad8;
    --ink: #555a60;
    --ink-soft: #7d8288;
    --footer-grey: #d3d4d6;
    --footer-text: #ffffff;
  }
  * { box-sizing: border-box; margin: 0; padding: 0; }
  html, body {
    width: 1200px; height: 1200px; overflow: hidden;
    background: var(--backdrop);
    font-family: "Open Sans", sans-serif;
  }
  .letterhead {
    position: absolute; left: 210px; top: 50px;
    width: 780px; height: 1100px;
    background: var(--paper);
    box-shadow: 0 6px 24px rgba(0,0,0,0.12);
    overflow: hidden;
  }
  .header-swoosh { position: absolute; left: 0; top: 0; width: 780px; height: 500px; }
  .brand {
    position: absolute; left: 46px; top: 92px;
    display: flex; align-items: center; gap: 12px;
  }
  .brand-mark {
    width: 44px; height: 44px; border-radius: 50%;
    border: 5px solid var(--brand-blue);
  }
  .brand-name {
    font-weight: 600; font-size: 17px; letter-spacing: 2px;
    color: var(--brand-blue); text-transform: uppercase;
  }
  .letter-body {
    position: absolute; left: 210px; top: 430px; width: 510px;
    font-weight: 300; font-size: 11.5px; line-height: 18px; color: var(--ink);
  }
  .salutation { margin-bottom: 14px; }
  .letter-body p { margin-bottom: 10px; }
  .sign-off { margin-top: 26px; }
  .signature {
    display: block; width: 170px; height: 58px; margin: 8px 0 4px;
    border-radius: 30px;
    background: linear-gradient(90deg, rgba(40,40,40,0.10), rgba(40,40,40,0.03));
  }
  .signer-title { color: var(--ink-soft); }
  .footer {
    position: absolute; left: 0; bottom: 0; width: 780px; height: 200px;
    background: var(--footer-grey);
  }
  .footer-rule {
    position: absolute; left: 0; top: 0; width: 100%; height: 5px;
    background: linear-gradient(90deg, var(--brand-blue), var(--deep-blue) 60%, var(--navy));
  }
  .contact-list {
    position: absolute; left: 40px; top: 74px; right: 30px;
    display: flex; justify-content: space-between; list-style: none;
  }
  .contact-item { display: flex; align-items: center; gap: 12px; }
  .contact-icon {
    width: 52px; height: 52px; border-radius: 50%;
    background: var(--brand-blue);
    display: flex; align-items: center; justify-content: center; flex: none;
  }
  .contact-text {
    color: var(--footer-text); font-weight: 400; font-size: 12.5px; line-height: 18px;
  }
  .contact-label { font-weight: 300; }
</style>
</head>
<body>
  <main class="letterhead">
    <svg class="header-swoosh" viewBox="0 0 780 500" aria-hidden="true">
      <defs>
        <linearGradient id="swooshFill" x1="1" y1="0" x2="0" y2="1">
          <stop offset="0" stop-color="#061046"/>
          <stop offset="0.35" stop-color="#0b3fa0"/>
          <stop offset="0.7" stop-color="#1b82cc"/>
          <stop offset="1" stop-color="#2f9ad8"/>
        </linearGradient>
      </defs>
      <path d="M712 0 H780 V215 C560 225 300 280 150 380 C90 420 40 450 0 478 V300 C120 180 420 70 712 0 Z" fill="url(#swooshFill)"/>
      <path d="M780 150 V215 C560 225 300 280 150 380 C300 260 560 190 780 150 Z" fill="#0b3fa0" opacity="0.45"/>
      <path d="M780 60 C560 130 300 220 160 330 C330 200 560 120 780 100 Z" fill="#ffffff" opacity="0.12"/>
    </svg>

    <div class="brand">
      <span class="brand-mark"></span>
      <span class="brand-name">Restora Homeworks</span>
    </div>

    <section class="letter-body">
      <p class="salutation">Greetings!</p>
      <p>Thank you for choosing our team to restore your property after the recent storm. We understand how stressful wind, hail and water damage can be, and we want to keep you informed at every stage of the work ahead.</p>
      <p>Our project manager has completed a full inspection of the roof, siding and windows, and the findings are summarized in the enclosed report. We have documented every area of damage with measurements and notes so that your insurance adjuster has a clear record of the loss. Once the claim is approved, our crew will secure the site, remove damaged materials and begin repairs using products that match or exceed the original specifications. We coordinate directly with your carrier to reduce delays, and we will schedule each phase around your needs so that daily life is disrupted as little as possible. Throughout the project you will receive regular updates, and a final walkthrough will confirm that everything has been returned to its pre-loss condition. If you have any questions about the estimate, the timeline or the warranty that covers our workmanship, please contact our office at any time. We look forward to restoring your home.</p>
      <p class="sign-off">Sincerely yours,</p>
      <span class="signature" role="img" aria-label="Handwritten signature of the company CEO"></span>
      <p class="signer-title">Restora Homeworks CEO</p>
    </section>

    <footer class="footer">
      <div class="footer-rule"></div>
      <ul class="contact-list">
        <li class="contact-item">
          <span class="contact-icon">
            <svg width="26" height="26" viewBox="0 0 24 24" aria-hidden="true"><path d="M12 2a7 7 0 0 0-7 7c0 5 7 13 7 13s7-8 7-13a7 7 0 0 0-7-7zm0 9.5A2.5 2.5 0 1 1 12 6.5a2.5 2.5 0 0 1 0 5z" fill="#fff"/></svg>
          </span>
          <div class="contact-text">
            <div class="contact-label">Address</div>
            <div>418 W Larkin Ave, Suite 112</div>
            <div>Maple Crest, IL 60118</div>
          </div>
        </li>
        <li class="contact-item">
          <span class="contact-icon">
            <svg width="24" height="24" viewBox="0 0 24 24" aria-hidden="true"><path d="M6.6 10.8a15 15 0 0 0 6.6 6.6l2.2-2.2a1 1 0 0 1 1-.25 11.4 11.4 0 0 0 3.6.57 1 1 0 0 1 1 1V20a1 1 0 0 1-1 1A17 17 0 0 1 3 4a1 1 0 0 1 1-1h3.5a1 1 0 0 1 1 1c0 1.25.2 2.45.57 3.6a1 1 0 0 1-.25 1z" fill="#fff"/></svg>
          </span>
          <div class="contact-text">
            <div class="contact-label">Contact</div>
            <div>Phone 847-555-0162</div>
            <div>Fax 847-555-0178</div>
          </div>
        </li>
        <li class="contact-item">
          <span class="contact-icon">
            <svg width="24" height="24" viewBox="0 0 24 24" aria-hidden="true"><path d="M12 3 5 12h4.5v9h5v-9H19z" fill="#fff"/></svg>
          </span>
          <div class="contact-text">
            <div>twitter.com/RestoraHome</div>
            <div>facebook.com/RestoraHomeworks</div>
            <div>www.restorahomeworks.com</div>
          </div>
        </li>
      </ul>
    </footer>
  </main>
</body>
</html>
```